Established research company needs fresh new powerpoint template

We need a powerpoint template for an established research and advisory company called Veltra Consulting. We develop policy, improve delivery, and build capacity within the public sector - mainly in relation to education and young people.

We have a long and successful track record in our sector, and have a grown-up, clean brand. We already have a logo (see attached) and want a simple, clean powerpoint template that incorporates our logo and colours and matches the brand identity on our website: https://www.veltraconsulting.example/

We need a title slide, a section header slide, a two-column slide for two panels of text, a two-column slide for one panel of text and one panel of imagery, and a single-column slide for text.

We want a template with built-in Styles so our team can make consistent-looking presentations without any manual formatting. We also want to use a font that will be compatible with devices used across a range of clients.

```html
<!DOCTYPE html>
<html lang="en">
<head>
<meta charset="utf-8">
<title>Veltra Consulting – Presentation Template</title>
<link href="https://fonts.googleapis.com/css2?family=Open+Sans:wght@400;600;700&family=Poppins:wght@500;600;700&display=swap" rel="stylesheet">
<style>
  :root{
    --orange:#ee7a33;
    --orange-soft:#fde6d6;
    --grey:#8b8f99;
    --grey-dark:#7d818b;
    --text:#555861;
    --line:#d8d9dd;
    --white:#ffffff;
  }
  *{box-sizing:border-box;margin:0;padding:0}
  html,body{width:1200px;height:4147px;overflow:hidden}
  body{
    background:linear-gradient(90deg,#f07f35 0%,#d98a5c 30%,#b29a93 62%,#9d9eaa 100%);
    font-family:"Open Sans",Arial,sans-serif;color:var(--text);
    position:relative;
  }
  .slide{
    position:absolute;left:44px;width:1112px;height:625px;background:var(--white);
    overflow:hidden;box-shadow:0 6px 18px rgba(60,40,30,.25);
  }
  .slide > *{position:absolute}
  .photo-shape{left:0;top:0}
  .brand{
    font-family:"Poppins",Arial,sans-serif;font-weight:600;color:var(--grey);
    display:flex;align-items:center;gap:10px;white-space:nowrap;
  }
  .brand::before{content:"";display:block;background:var(--orange);flex:none}
  .brand--large{font-size:30px;letter-spacing:-.3px}
  .brand--large::before{width:16px;height:16px}
  .brand--small{top:44px;right:28px;font-size:17px}
  .brand--small::before{width:10px;height:10px}
  .divider{width:2px;background:var(--line)}
  .cover-title{font-family:"Poppins",Arial,sans-serif;font-weight:700;font-size:31px;color:var(--grey);letter-spacing:.3px}
  .cover-sub{font-size:15px;line-height:23px;width:400px}
  .footer-url{left:30px;top:592px;font-size:12px;color:#8a8d94}
  .page-no{right:30px;top:592px;font-size:12px;color:#8a8d94}
  .page-no b{color:var(--orange);font-weight:600}
  .heading{
    left:29px;top:30px;font-family:"Poppins",Arial,sans-serif;font-weight:600;font-size:45px;color:var(--grey);
  }
  .heading em{font-style:normal;color:var(--orange)}
  .section-no{
    left:520px;top:196px;font-family:"Poppins",Arial,sans-serif;font-weight:700;font-size:34px;color:var(--orange);
  }
  .section-no::before{
    content:"";position:absolute;left:-6px;top:4px;width:44px;height:44px;border-radius:50%;
    background:var(--orange-soft);z-index:-1;
  }
  .section-title{left:520px;top:285px;font-family:"Poppins",Arial,sans-serif;font-weight:700;font-size:58px;color:var(--grey);letter-spacing:.5px}
  .section-text{left:520px;top:365px;width:560px;font-size:17px;line-height:31px}
  .body-text{font-size:17px;line-height:32px}
  .img-block{border-radius:4px}
  .work-item{width:520px;display:flex;gap:14px}
  .work-item > div{width:448px}
  .work-icon{flex:none;width:58px;height:58px;margin-top:-6px}
  .work-item h3{font-family:"Open Sans",Arial,sans-serif;font-weight:600;font-size:18px;letter-spacing:.2px;color:var(--grey-dark);margin-bottom:5px;white-space:nowrap}
  .work-item h3.accent{color:var(--orange)}
  .work-item p{font-size:15px;line-height:29px}
  .skills{list-style:none;left:29px;top:330px;width:1060px;font-size:17px;line-height:32px}
  .skills li{position:relative;padding-left:30px}
  .skills li svg{position:absolute;left:0;top:9px}
  .email{display:flex;align-items:center;gap:12px;font-size:21px;color:#4a4d55}
</style>
</head>
<body>

<!-- Title slide -->
<section class="slide" style="top:55px">
  <svg class="photo-shape" width="1112" height="500" viewBox="0 0 1112 500">
    <defs>
      <linearGradient id="classroomTone" x1="0" y1="0" x2="1" y2="1">
        <stop offset="0" stop-color="#c9b39c"/><stop offset=".45" stop-color="#b99679"/>
        <stop offset=".75" stop-color="#8c8878"/><stop offset="1" stop-color="#5f6e66"/>
      </linearGradient>
    </defs>
    <path d="M0 16 H1112 V222 C900 440 620 486 460 478 C260 468 90 420 0 356 Z" fill="var(--orange)"/>
    <path d="M0 0 H1112 V205 C900 420 620 468 460 460 C260 450 90 402 0 340 Z" fill="url(#classroomTone)" role="img" aria-label="Photo of pupils raising hands in a classroom"/>
  </svg>
  <div class="brand brand--large" style="left:28px;top:530px">Veltra Consulting</div>
  <div class="divider" style="left:388px;top:508px;height:96px"></div>
  <h1 class="cover-title" style="left:437px;top:505px">BETTER PUBLIC SERVICES</h1>
  <p class="cover-sub" style="left:437px;top:552px">We help the public sector solve problems and deliver effectively.</p>
</section>

<!-- Section header slide -->
<section class="slide" style="top:735px">
  <svg class="photo-shape" width="520" height="600" viewBox="0 0 520 600">
    <defs>
      <linearGradient id="teamTone" x1="0" y1="0" x2="1" y2="1">
        <stop offset="0" stop-color="#d8cbbb"/><stop offset=".5" stop-color="#9a7d67"/><stop offset="1" stop-color="#4b4a4e"/>
      </linearGradient>
    </defs>
    <path d="M488 0 C536 210 420 460 0 590 L0 578 C410 450 520 210 474 0 Z" fill="var(--orange)"/>
    <path d="M0 0 H476 C520 210 410 452 0 578 Z" fill="url(#teamTone)" role="img" aria-label="Photo of a team working together around a laptop"/>
  </svg>
  <div class="brand brand--small">Veltra Consulting</div>
  <div class="section-no">1.</div>
  <h2 class="section-title">INTRODUCTION</h2>
  <p class="section-text">We are a research and advisory company with a track-record in developing policy, improving delivery, and building capacity within the public sector.</p>
  <div class="footer-url">www.veltraconsulting.example</div>
  <div class="page-no">Page: <b>2</b></div>
</section>

<!-- Text and imagery slide -->
<section class="slide" style="top:1413px">
  <h2 class="heading"><em>Who</em> We Are</h2>
  <div class="brand brand--small">Veltra Consulting</div>
  <p class="body-text" style="left:29px;top:208px;width:470px">We have in-depth experience of working with the public sector, in the UK and overseas, in education, local government, health and social care. We have expertise and a proven track record in developing policy and strategy, solving delivery problems, undertaking national evaluations and writing influential research reports, advising on organisational reform, and facilitating workshops and conferences.</p>
  <div class="img-block" style="left:556px;top:121px;width:255px;height:372px;background:linear-gradient(160deg,#8a7a5e,#c8c2b3 50%,#4f6f8e)" role="img" aria-label="Photo of a facilitator presenting at a whiteboard"></div>
  <div class="img-block" style="left:828px;top:179px;width:255px;height:372px;background:linear-gradient(160deg,#3e444c,#8a7b6e 50%,#b79f84)" role="img" aria-label="Photo of colleagues in discussion at a meeting table"></div>
  <div class="footer-url">www.veltraconsulting.example</div>
  <div class="page-no">Page: <b>3</b></div>
</section>

<!-- Two text panels slide -->
<section class="slide" style="top:2093px">
  <h2 class="heading"><em>Our</em> Work</h2>
  <div class="brand brand--small">Veltra Consulting</div>

  <div class="work-item" style="left:25px;top:168px">
    <svg class="work-icon" viewBox="0 0 58 58"><circle cx="29" cy="31" r="24" fill="#eeeff1"/><rect x="14" y="12" width="30" height="22" rx="2" fill="none" stroke="var(--grey)" stroke-width="2"/><path d="M19 29v-5M24 29v-9M29 29v-7" stroke="var(--grey)" stroke-width="2"/><circle cx="37" cy="27" r="6" fill="none" stroke="var(--orange)" stroke-width="2"/><path d="M41 31l6 6" stroke="var(--orange)" stroke-width="2"/></svg>
    <div><h3>STRATEGIC PLANNING</h3><p>We can support you to develop policies and strategies and design performance and delivery systems to implement these. We have a strong record in engaging stakeholders in designing systems and strategic planning.</p></div>
  </div>

  <div class="work-item" style="left:575px;top:168px">
    <svg class="work-icon" viewBox="0 0 58 58"><circle cx="29" cy="31" r="24" fill="#eeeff1"/><g fill="none" stroke="var(--orange)" stroke-width="2"><circle cx="29" cy="12" r="4"/><path d="M23 24a6 6 0 0 1 12 0"/><path d="M29 24v6M16 30h26M16 30v4M29 30v4M42 30v4"/><circle cx="16" cy="38" r="3.5"/><circle cx="29" cy="38" r="3.5"/><circle cx="42" cy="38" r="3.5"/><path d="M11 48a5 5 0 0 1 10 0M24 48a5 5 0 0 1 10 0M37 48a5 5 0 0 1 10 0"/></g></svg>
    <div><h3 class="accent">ORGANISATIONAL CAPACITY</h3><p>We will transfer skills and knowledge in every project we undertake. In addition we can work with you to create dedicated performance and delivery capability within your organization. We coach and train top teams and facilitate partner and stakeholder workshops.</p></div>
  </div>

  <div class="work-item" style="left:25px;top:366px">
    <svg class="work-icon" viewBox="0 0 58 58"><circle cx="29" cy="31" r="24" fill="var(--orange-soft)"/><g fill="none" stroke="var(--orange)" stroke-width="2"><circle cx="29" cy="22" r="9"/><path d="M25 31v6h8v-6M26 41h6"/><circle cx="29" cy="22" r="3"/><path d="M29 8v3M18 12l2 2M40 12l-2 2M15 22h3M43 22h-3"/></g></svg>
    <div><h3 class="accent">DELIVERY, EFFICIENCY AND INNOVATION</h3><p>We can assess &amp; strengthen programme implementation, review progress of established projects, and provide rapid feedback from delivery partners. We can also work with you to reconfigure services and resources to maximise value for money.</p></div>
  </div>

  <div class="work-item" style="left:575px;top:397px">
    <svg class="work-icon" viewBox="0 0 58 58"><circle cx="29" cy="31" r="24" fill="#eeeff1"/><g fill="none" stroke="var(--grey)" stroke-width="2"><rect x="14" y="10" width="24" height="32" rx="2"/><path d="M18 16h16M18 21h10"/><circle cx="32" cy="32" r="8"/><path d="M28 32l3 3 5-6" stroke="var(--orange)"/><path d="M38 38l7 7"/></g></svg>
    <div><h3>RESEARCH AND EVALUATION</h3><p>We are skilled in evaluating the impact of policies, using both qualitative and quantitative techniques, and can undertake bespoke research projects to inform policy making and delivery.</p></div>
  </div>

  <div class="footer-url">www.veltraconsulting.example</div>
  <div class="page-no">Page: <b>4</b></div>
</section>

<!-- Single-column text slide -->
<section class="slide" style="top:2771px">
  <h2 class="heading"><em>Join</em> the Team</h2>
  <div class="brand brand--small">Veltra Consulting</div>
  <p class="body-text" style="left:29px;top:174px;width:1060px">We are always interested in talking to dynamic, talented people who share our values and commitment to working with the public sector to build capacity, improve delivery, and achieve better outcomes.</p>
  <p class="body-text" style="left:29px;top:263px;font-weight:600;color:#4a4d55">The skills we look for in people to join our team at Veltra Consulting are:</p>
  <ul class="skills">
    <li><svg width="15" height="15" viewBox="0 0 15 15"><circle cx="7.5" cy="7.5" r="7.5" fill="var(--orange)"/><path d="M4 7.6l2.4 2.4L11 5.3" fill="none" stroke="#fff" stroke-width="1.8"/></svg>Excellent communication skills, both written and oral;</li>
    <li><svg width="15" height="15" viewBox="0 0 15 15"><circle cx="7.5" cy="7.5" r="7.5" fill="var(--orange)"/><path d="M4 7.6l2.4 2.4L11 5.3" fill="none" stroke="#fff" stroke-width="1.8"/></svg>Outstanding strategic-thinking, analytical, and problem-solving abilities;</li>
    <li><svg width="15" height="15" viewBox="0 0 15 15"><circle cx="7.5" cy="7.5" r="7.5" fill="var(--orange)"/><path d="M4 7.6l2.4 2.4L11 5.3" fill="none" stroke="#fff" stroke-width="1.8"/></svg>Qualitative and quantitative research skills;</li>
    <li><svg width="15" height="15" viewBox="0 0 15 15"><circle cx="7.5" cy="7.5" r="7.5" fill="var(--orange)"/><path d="M4 7.6l2.4 2.4L11 5.3" fill="none" stroke="#fff" stroke-width="1.8"/></svg>The ability to work with and influence senior stakeholders; and</li>
    <li><svg width="15" height="15" viewBox="0 0 15 15"><circle cx="7.5" cy="7.5" r="7.5" fill="var(--orange)"/><path d="M4 7.6l2.4 2.4L11 5.3" fill="none" stroke="#fff" stroke-width="1.8"/></svg>Expertise and a track-record of success in a specific area of the public sector – such as education, special educational needs, mental health, or children’s services.</li>
  </ul>
  <div class="footer-url">www.veltraconsulting.example</div>
  <div class="page-no">Page: <b>5</b></div>
</section>

<!-- Closing slide -->
<section class="slide" style="top:3451px">
  <svg class="photo-shape" width="1112" height="500" viewBox="0 0 1112 500">
    <defs>
      <linearGradient id="pupilsTone" x1="0" y1="0" x2="1" y2="1">
        <stop offset="0" stop-color="#8d7a5f"/><stop offset=".45" stop-color="#c49a74"/>
        <stop offset=".75" stop-color="#8f8c7a"/><stop offset="1" stop-color="#a69272"/>
      </linearGradient>
    </defs>
    <path d="M0 16 H1112 V222 C900 446 620 484 460 478 C260 470 90 424 0 362 Z" fill="var(--orange)"/>
    <path d="M0 0 H1112 V205 C900 428 620 466 460 460 C260 452 90 406 0 346 Z" fill="url(#pupilsTone)" role="img" aria-label="Photo of smiling pupils at their desks in a classroom"/>
  </svg>
  <div class="brand brand--large" style="left:28px;top:532px">Veltra Consulting</div>
  <div class="divider" style="left:398px;top:510px;height:92px"></div>
  <h2 class="cover-title" style="left:461px;top:512px">THANK YOU</h2>
  <div class="email" style="left:461px;top:556px">
    <svg width="20" height="15" viewBox="0 0 20 15"><rect width="20" height="15" rx="2" fill="var(--orange)"/><path d="M1 2l9 7 9-7" fill="none" stroke="#fff" stroke-width="1.6"/></svg>
    info@veltraconsulting.example
  </div>
</section>

</body>
</html>
```